Criação de Logo + Papelaria + Manual Básico para Arquitetura
" Somos uma empresa pequena, eu e a minha sócia Clarice, atendemos o cliente, fazemos o levantamento de medidas e necessidades do cliente, desenvolvemos o projeto desde o início em 3D colorido, depois o projeto executivo e acompanhamento de obras. Estamos presentes no processo do início ao fim. Buscamos sempre atender o cliente da melhor maneira possível, sempre estando a par de todo o projeto. "

```html
<!DOCTYPE html>
<html lang="pt-BR">
<head>
<meta charset="UTF-8">
<title>RC Estúdio – Envelope</title>
<link rel="stylesheet" href="https://fonts.googleapis.com/css2?family=Cormorant+Garamond:wght@400;500&family=Montserrat:wght@400&display=swap">
<style>
  :root {
    --backdrop: #eeece9;
    --envelope-grey: #8b8b8c;
    --flap-grey: #9a9a9b;
    --paper-white: #ffffff;
    --blush: #d9a593;
    --ink-grey: #7d7d7e;
    --serif: "Cormorant Garamond", Georgia, serif;
    --sans: "Montserrat", Arial, sans-serif;
  }
  * { margin: 0; padding: 0; box-sizing: border-box; }
  html, body { width: 1200px; height: 1200px; overflow: hidden; }
  body { background: var(--backdrop); position: relative; }

  .envelope-back {
    position: absolute;
    left: 168px; top: 228px;
    width: 864px; height: 372px;
    background: var(--envelope-grey);
    clip-path: polygon(5% 0, 95% 0, 100% 13%, 100% 100%, 0 100%, 0 13%);
  }
  .brand-lockup {
    position: absolute;
    left: 54px; top: 96px;
    text-align: center;
    color: var(--paper-white);
  }
  .brand-initials {
    font-family: var(--serif);
    font-weight: 500;
    font-size: 84px;
    line-height: 0.9;
    letter-spacing: -2px;
  }
  .brand-word {
    font-family: var(--serif);
    font-weight: 500;
    font-size: 20px;
    letter-spacing: 6px;
    margin-top: 4px;
  }
  .brand-initials-large {
    position: absolute;
    left: 290px; top: 10px;
    font-family: var(--serif);
    font-weight: 500;
    font-size: 400px;
    line-height: 0.95;
    letter-spacing: -14px;
    color: var(--paper-white);
  }

  .envelope-front {
    position: absolute;
    left: 324px; top: 648px;
    width: 720px; height: 312px;
    background: var(--paper-white);
    overflow: hidden;
  }
  .envelope-front .inner-flap {
    position: absolute; left: 0; top: 0;
    width: 100%; height: 40px;
  }
  .front-logo {
    position: absolute;
    left: 0; right: 0; top: 160px;
    text-align: center;
    font-family: var(--serif);
    font-weight: 500;
    font-size: 46px;
    line-height: 1;
    letter-spacing: -1px;
    color: var(--ink-grey);
  }
  .contact {
    position: absolute;
    left: 0; right: 0;
    display: flex; justify-content: center; align-items: center; gap: 6px;
    font-family: var(--sans);
    font-size: 11px;
    color: var(--ink-grey);
  }
  .contact-address { top: 234px; }
  .contact-phone { top: 264px; }
  .contact svg { width: 12px; height: 12px; fill: var(--ink-grey); }
</style>
</head>
<body>

  <section class="envelope-back">
    <div class="brand-lockup">
      <div class="brand-initials">RC</div>
      <div class="brand-word">ESTÚDIO</div>
    </div>
    <div class="brand-initials-large">RC</div>
  </section>

  <section class="envelope-front">
    <svg class="inner-flap" viewBox="0 0 720 40" preserveAspectRatio="none" aria-hidden="true">
      <polygon points="0,0 720,0 720,40 690,14 30,14 0,40" fill="var(--flap-grey)"/>
    </svg>
    <div class="front-logo">RC</div>
    <p class="contact contact-address">
      <svg viewBox="0 0 24 24" aria-hidden="true"><path d="M12 2a7 7 0 0 0-7 7c0 5.2 7 13 7 13s7-7.8 7-13a7 7 0 0 0-7-7zm0 9.5A2.5 2.5 0 1 1 12 6.5a2.5 2.5 0 0 1 0 5z"/></svg>
      Rua xxxxxxxxxxxxxxxxx, nº - Bairro - Cidade - MG | Cep: 00000-000
    </p>
    <p class="contact contact-phone">
      <svg viewBox="0 0 24 24" aria-hidden="true"><path d="M6.6 10.8a15.1 15.1 0 0 0 6.6 6.6l2.2-2.2a1 1 0 0 1 1-.25 11.4 11.4 0 0 0 3.6.57 1 1 0 0 1 1 1V20a1 1 0 0 1-1 1A17 17 0 0 1 3 4a1 1 0 0 1 1-1h3.5a1 1 0 0 1 1 1c0 1.25.2 2.45.57 3.57a1 1 0 0 1-.25 1z"/></svg>
      (00) 0000-0000
    </p>
  </section>

</body>
</html>
```